Tello Haulage Junk Removal Postcard

I am looking to have a postcard made for my junk removal company. Details:
size: 6"x9"
I would like to keep it clean and simple. Our company colors are pink, blue and white. You can find the colors and info on the company and what we do on our website which is www.tellohaulage.example .
I've attached a sample of a postcard that was made on ArtHive for another junk removal company. I like the way the attached one looks.

```html
<!DOCTYPE html>
<html lang="en">
<head>
<meta charset="utf-8">
<title>Tello Haulage Postcard</title>
<link rel="stylesheet" href="https://fonts.googleapis.com/css2?family=Montserrat:wght@600;700;800;900&family=Oswald:wght@500;700&family=Lato:wght@400;700&display=swap">
<style>
  :root {
    --blue: #0f5fae;
    --pink: #e8118b;
    --white: #ffffff;
    --paper: #f2f2f2;
    --red: #c8202f;
    --ink: #1d1d1d;
    --stage: #e4e4e6;
  }
  * { box-sizing: border-box; margin: 0; padding: 0; }
  html, body { width: 895px; height: 1200px; overflow: hidden; background: var(--stage); }
  .canvas { position: relative; width: 895px; height: 1200px; }
  .card { position: absolute; transform-origin: 0 0; transform: scale(0.5424); overflow: hidden; font-family: "Montserrat", sans-serif; }
  .card-front { left: 111px; top: 130px; width: 1241px; height: 827px; background: var(--paper); }
  .card-back { left: 112px; top: 654px; width: 1238px; height: 823px; background: var(--white); }
  .abs { position: absolute; }
  .shapes { position: absolute; left: 0; top: 0; }

  .brand-name { font-family: "Montserrat", sans-serif; font-weight: 800; color: var(--pink); font-size: 44px; letter-spacing: -0.5px; white-space: nowrap; }
  .find-us { left: 860px; top: 56px; color: var(--white); font-weight: 700; font-size: 32px; }
  .social { top: 55px; width: 44px; height: 44px; border-radius: 50%; background: var(--white); opacity: 0.92; }

  .photo { left: 590px; top: 108px; width: 651px; height: 432px; background: linear-gradient(100deg, #e9e9e9 0%, #8dc63f 35%, #6aa52c 55%, #f0f0f0 70%, #e86a1e 85%, #2b3444 100%); }

  .headline { left: 62px; top: 222px; color: var(--white); font-weight: 800; font-size: 124px; letter-spacing: 6px; line-height: 1; }
  .tagline { left: 70px; top: 345px; color: var(--white); font-weight: 800; font-size: 38px; }

  .service-list { left: 70px; top: 415px; list-style: none; }
  .service-list li { display: flex; align-items: center; height: 47.5px; color: var(--white); font-weight: 800; font-size: 22px; letter-spacing: 0.5px; }
  .service-list svg { width: 40px; height: 38px; margin-right: 28px; }
  .service-list .sep { width: 2px; height: 26px; background: var(--white); margin-right: 10px; }

  .burst { left: 348px; top: 440px; width: 250px; height: 200px; }
  .burst-text { left: 348px; top: 488px; width: 250px; text-align: center; }
  .burst-free { color: var(--pink); font-weight: 900; font-size: 54px; line-height: 0.95; }
  .burst-est { color: var(--blue); font-weight: 800; font-size: 27px; line-height: 1; }
  .burst-pill { display: inline-block; margin-top: 5px; background: var(--blue); color: var(--white); font-weight: 800; font-size: 11px; padding: 2px 10px; border-radius: 9px; letter-spacing: 0.5px; }

  .book { left: 60px; top: 678px; color: var(--pink); font-family: "Oswald", sans-serif; font-weight: 700; font-size: 40px; letter-spacing: -0.5px; line-height: 1; }
  .fine-print { left: 62px; top: 722px; color: var(--ink); font-size: 12px; font-weight: 600; }
  .price { left: 444px; top: 668px; color: var(--white); font-family: "Oswald", sans-serif; font-weight: 700; font-size: 70px; line-height: 1; }
  .front-web { left: 68px; top: 766px; color: var(--white); font-weight: 700; font-size: 31px; }

  .hours { display: flex; align-items: center; }
  .hours-pill { background: var(--blue); border: 3px solid var(--white); border-radius: 40px; color: var(--white); font-family: "Oswald", sans-serif; font-weight: 700; font-style: italic; line-height: 1; }
  .hours-clock { border-radius: 50%; background: var(--red); border: 4px solid var(--white); display: flex; align-items: center; justify-content: center; }
  .hours-label { font-family: "Oswald", sans-serif; font-weight: 700; font-style: italic; line-height: 1.05; text-transform: uppercase; }
  .hours-label .l1 { display: block; color: var(--white); }
  .hours-label .l2 { display: inline-block; background: var(--blue); color: var(--white); padding: 0 10px; }

  .front-hours { left: 810px; top: 553px; }
  .front-hours .hours-pill { font-size: 52px; padding: 4px 70px 4px 20px; }
  .front-hours .hours-clock { width: 66px; height: 66px; margin-left: -60px; }
  .front-hours .hours-label { font-size: 30px; margin-left: 8px; }

  .phone { display: flex; align-items: center; color: var(--white); font-weight: 900; line-height: 1; }
  .phone-icon { border-radius: 50%; background: var(--blue); border: 3px solid var(--white); display: flex; align-items: center; justify-content: center; }
  .front-phone { left: 672px; top: 625px; font-size: 62px; }
  .front-phone .phone-icon { width: 52px; height: 52px; margin-right: 16px; }

  .perks { left: 693px; top: 710px; width: 475px; height: 76px; }
  .perk { position: absolute; top: 0; width: 76px; height: 76px; border-radius: 50%; background: var(--blue); border: 2px dashed var(--white); box-shadow: 0 3px 0 var(--pink); color: var(--white); font-family: "Oswald", sans-serif; font-weight: 500; font-size: 12px; line-height: 1.2; text-align: center; display: flex; align-items: center; justify-content: center; }
  .perk-line { position: absolute; top: 37px; left: 38px; right: 38px; border-top: 2px dashed var(--blue); }

  /* back */
  .story-bar { left: 70px; top: 48px; width: 3px; height: 122px; background: var(--white); }
  .story-title { left: 90px; top: 40px; color: var(--white); font-weight: 700; font-size: 40px; }
  .story-title span { color: var(--pink); }
  .story-lead { left: 90px; top: 100px; width: 440px; }
  .story-body { left: 68px; width: 470px; }
  .story-text { color: var(--white); font-family: "Lato", sans-serif; font-size: 17px; line-height: 1.38; }
  .proud { left: 66px; top: 400px; color: var(--pink); font-weight: 800; font-size: 50px; line-height: 1; }
  .proud-sub { left: 66px; top: 456px; color: var(--blue); font-weight: 800; font-size: 30px; }

  .back-hours { left: 73px; top: 544px; }
  .back-hours .hours-pill { font-size: 76px; padding: 4px 80px 4px 30px; }
  .back-hours .hours-clock { width: 92px; height: 92px; margin-left: -70px; }
  .back-hours .hours-label { font-size: 42px; margin-left: 10px; }
  .back-phone { left: 73px; top: 643px; font-size: 66px; }
  .back-phone .phone-icon { width: 54px; height: 54px; margin-right: 16px; }
  .back-web { left: 88px; top: 755px; color: var(--white); font-weight: 700; font-size: 30px; letter-spacing: 5.5px; }

  .back-brand { left: 770px; top: 110px; }
  .stamp { left: 1036px; top: 63px; width: 133px; height: 132px; border: 1.5px solid var(--ink); }
  .address-line { left: 813px; width: 356px; height: 1.5px; background: var(--ink); }
</style>
</head>
<body>
<main class="canvas">

  <section class="card card-front" aria-label="Postcard front">
    <svg class="shapes" width="1241" height="827" viewBox="0 0 1241 827">
      <polygon points="835,0 1241,0 1241,140 775,140" fill="var(--pink)"/>
      <polygon points="798,56 812,56 772,140 758,140" fill="var(--blue)"/>
    </svg>

    <div class="abs photo" role="img" aria-label="Photo of a green haulage truck and a smiling worker in hi-vis overalls holding a broom beside a bin"></div>

    <svg class="shapes" width="1241" height="827" viewBox="0 0 1241 827">
      <polygon points="0,205 588,205 725,540 700,660 590,660 560,827 0,827" fill="var(--blue)"/>
      <polygon points="0,336 610,336 635,398 0,398" fill="var(--pink)"/>
      <polygon points="655,540 1241,540 1241,697 598,697" fill="var(--pink)"/>
      <polygon points="640,582 650,582 588,697 578,697" fill="var(--white)"/>
      <polygon points="598,697 1241,697 1241,800 560,800 560,760" fill="var(--white)"/>
      <polygon points="545,800 1241,800 1241,827 532,827" fill="var(--blue)"/>
      <polygon points="0,667 430,667 410,752 0,752" fill="var(--white)"/>
      <polygon points="430,657 590,657 560,752 410,752" fill="var(--pink)"/>
      <polygon points="540,752 560,752 538,827 518,827" fill="var(--white)"/>
    </svg>

    <div class="abs brand-name" style="left:85px; top:95px;">Tello Haulage</div>

    <div class="abs find-us">Find Us</div>
    <span class="abs social" style="left:1005px;"></span>
    <span class="abs social" style="left:1067px;"></span>
    <span class="abs social" style="left:1129px;"></span>

    <h1 class="abs headline">RELAX</h1>
    <p class="abs tagline">WE DO THE DIRTY WORK</p>

    <ul class="abs service-list">
      <li><svg viewBox="0 0 40 38" fill="none" stroke="#fff" stroke-width="2"><path d="M4 18 20 5 36 18"/><rect x="9" y="16" width="22" height="19"/><rect x="17" y="24" width="6" height="11"/></svg><span class="sep"></span>RESIDENTIAL</li>
      <li><svg viewBox="0 0 40 38" fill="none" stroke="#fff" stroke-width="2"><rect x="8" y="4" width="24" height="31"/><path d="M13 10h4M23 10h4M13 17h4M23 17h4M13 24h4M23 24h4"/></svg><span class="sep"></span>COMMERCIAL</li>
      <li><svg viewBox="0 0 40 38" fill="none" stroke="#fff" stroke-width="2"><circle cx="14" cy="14" r="8"/><path d="M14 22v13M4 35h32"/><path d="M26 12h10l-5-6z"/></svg><span class="sep"></span>OUTSIDE</li>
      <li><svg viewBox="0 0 40 38" fill="none" stroke="#fff" stroke-width="2"><circle cx="18" cy="7" r="4"/><path d="M18 11v12l-6 12M18 23l6 12M10 17h16"/><path d="M28 26h8v9h-8z"/></svg><span class="sep"></span>CURBSIDE</li>
      <li><svg viewBox="0 0 40 38" fill="none" stroke="#fff" stroke-width="2"><path d="M6 11 20 4 34 11v17L20 35 6 28z"/><path d="M6 11l14 7 14-7M20 18v17"/><circle cx="31" cy="30" r="5"/></svg><span class="sep"></span>OTHER</li>
    </ul>

    <svg class="abs burst" viewBox="-125 -100 250 200" aria-hidden="true">
      <polygon transform="translate(6,8)" fill="var(--blue)" opacity="0.6" points="0,-96 22,-72 55,-84 58,-52 98,-45 80,-18 110,6 80,26 96,56 58,60 50,92 20,76 0,98 -20,76 -50,92 -58,60 -96,56 -80,26 -110,6 -80,-18 -98,-45 -58,-52 -55,-84 -22,-72"/>
      <polygon fill="var(--white)" stroke="var(--pink)" stroke-width="5" points="0,-96 22,-72 55,-84 58,-52 98,-45 80,-18 110,6 80,26 96,56 58,60 50,92 20,76 0,98 -20,76 -50,92 -58,60 -96,56 -80,26 -110,6 -80,-18 -98,-45 -58,-52 -55,-84 -22,-72"/>
    </svg>
    <div class="abs burst-text">
      <div class="burst-free">FREE</div>
      <div class="burst-est">ESTIMATE</div>
      <span class="burst-pill">CALL US NOW</span>
    </div>

    <p class="abs book">BOOK TODAY AND SAVE</p>
    <p class="abs fine-print">*Not Valid On Single Item Or Minimum Charge Pickups.</p>
    <p class="abs price">$30</p>
    <p class="abs front-web">www.tellohaulage.example</p>

    <div class="abs hours front-hours">
      <span class="hours-pill">24/7</span>
      <span class="hours-clock"><svg width="40" height="40" viewBox="0 0 40 40" fill="none" stroke="#fff" stroke-width="3"><circle cx="20" cy="20" r="16"/><path d="M20 10v10l7 5"/></svg></span>
      <span class="hours-label"><span class="l1" style="color:var(--white)">Customer</span><span class="l2">Services</span></span>
    </div>

    <div class="abs phone front-phone">
      <span class="phone-icon"><svg width="26" height="26" viewBox="0 0 24 24" fill="#fff"><path d="M6.6 10.8a15 15 0 0 0 6.6 6.6l2.2-2.2a1 1 0 0 1 1-.25 11.4 11.4 0 0 0 3.6.57 1 1 0 0 1 1 1V20a1 1 0 0 1-1 1A17 17 0 0 1 3 4a1 1 0 0 1 1-1h3.5a1 1 0 0 1 1 1c0 1.25.2 2.45.57 3.57a1 1 0 0 1-.25 1z"/></svg></span>
      555-014-2290
    </div>

    <div class="abs perks">
      <span class="perk-line"></span>
      <span class="perk" style="left:0;">Call Us<br>Today</span>
      <span class="perk" style="left:133px;">Same Day<br>Service</span>
      <span class="perk" style="left:266px;">Covid-19<br>Compliant.</span>
      <span class="perk" style="left:399px;">Best Price<br>Guaranteed</span>
    </div>
  </section>

  <section class="card card-back" aria-label="Postcard back">
    <svg class="shapes" width="1238" height="823" viewBox="0 0 1238 823">
      <polygon points="0,0 500,0 782,823 0,823" fill="var(--blue)"/>
      <polygon points="500,0 512,0 790,823 778,823" fill="var(--white)"/>
      <polygon points="512,0 606,0 785,800" fill="var(--pink)"/>
      <polygon points="0,383 612,383 657,513 0,513" fill="var(--white)"/>
      <polygon points="0,513 657,513 735,738 0,738" fill="var(--pink)"/>
    </svg>

    <span class="abs story-bar"></span>
    <h2 class="abs story-title">Our <span>Story</span></h2>
    <p class="abs story-text story-lead">Family owned and locally operated,<br>Tello Haulage brings 20+ years of moving and junk removal experience to each and every job.</p>
    <p class="abs story-text story-body" style="top:188px;">Founded by husband and wife team, Marco + Elena, the pair dove into the industry down in Harbor City with Brightline Movers in 2010 and its sister company Brightline Junk in 2011.</p>
    <p class="abs story-text story-body" style="top:295px;">Built from the ground up, both companies continue thriving today with a sterling reputation throughout the community and predominantly referral-based clientele.</p>

    <p class="abs proud">Proud To Be</p>
    <p class="abs proud-sub">Family Owned, Locally Operated</p>

    <div class="abs hours back-hours">
      <span class="hours-pill">24/7</span>
      <span class="hours-clock"><svg width="54" height="54" viewBox="0 0 40 40" fill="none" stroke="#fff" stroke-width="3"><circle cx="20" cy="20" r="16"/><path d="M20 10v10l7 5"/></svg></span>
      <span class="hours-label"><span class="l1">Customer</span><span class="l2">Services</span></span>
    </div>

    <div class="abs phone back-phone">
      <span class="phone-icon"><svg width="28" height="28" viewBox="0 0 24 24" fill="#fff"><path d="M6.6 10.8a15 15 0 0 0 6.6 6.6l2.2-2.2a1 1 0 0 1 1-.25 11.4 11.4 0 0 0 3.6.57 1 1 0 0 1 1 1V20a1 1 0 0 1-1 1A17 17 0 0 1 3 4a1 1 0 0 1 1-1h3.5a1 1 0 0 1 1 1c0 1.25.2 2.45.57 3.57a1 1 0 0 1-.25 1z"/></svg></span>
      555-014-2290
    </div>

    <p class="abs back-web">www.tellohaulage.example</p>

    <div class="abs brand-name back-brand" style="font-size:36px;">Tello Haulage</div>
    <div class="abs stamp" aria-label="Stamp area"></div>
    <span class="abs address-line" style="top:460px;"></span>
    <span class="abs address-line" style="top:540px;"></span>
    <span class="abs address-line" style="top:620px;"></span>
  </section>

</main>
</body>
</html>
```